This is my scope and requirements:
Labelling project:
This is related to the Label project I also opened up. (The Brisk Owl Organic & Natural Soaps needs a good business card (Contest) )
I have attached an initial draft at a logo I tried to come up with for a business card and labelling/marketing. I am hoping that you can take this logo and 'run with it' to finesse it, make it look unique and professional. If you need to change it, I am open to ideas.
I find that labelling/packaging is hard for me to make it look 'professional' so I am coming to the experts!
I am looking for label designs for 2 different bottles and 2 different bar soaps:
1) Organic Bar Soap (2 possibilities: 1) Kraft 'cigar' band around soap with twine, 2) Kraft soap box with Kraft sticker Labels
2) Natural Olive Oil Based Bar Soap (labelling can be same as Organic but with distinct info)
3) Organic Hand Washes (clear square bottles, 250ml with natural pump)
4) Natural Olive Oil Based Body Wash (taper bottle 200ml with metal silver disc top caps)
I am a start up at home company making Organic and Natural Bar soaps, hand soaps, body washes.
All of my ingredients are organic or natural and will include natural essential oils, exfoliants, natural powders/colours, etc.
Some of the names are: Quillomé (feisty, energetic soap), Dunes (more of a sandalwood earthy tones with a sandalwood powder exfoliant), Frost (maybe changing this name - fresh scented), Amber Thyme (lemongrass/ginger, exfoliants), etc....
If you need more information, please let me know!
Please find attached: Kraft Paper I am looking at to possibly wrap the Bar Soaps in (I like the different colour concept and am trying to decide between diff colours of Ned Parrow paper to wrap around or plain kraft paper.. whichever the new logo concept will look best with.
The bottles I will be using for the hand soap (250ml square) and the body wash (200ml tapered)
OLD POST:
Hello! I am a start up business that is specializing in making luxury organic bar soaps, natural olive oil bar soaps, organic hand wash, natural olive oil body wash/shower gel that will include essential oils, exfoliants, natural powders, etc. (also accessories: wood soap dishes, etc) .. I am looking for a great designer that can provide me with the business card and labelling designs! I appreciate feedback, ideas on how I can receive a great design to help sell my products!
I am attaching my initial logo design that I would like to keep - but am looking for someone to 'finesse' it or make it more professional/unique looking.
Again, this is hand in hand with the business card project I submitted.
Thanks!
Verla
Updates
I am sorry for the lack of direction or Scope of the project. I am new at this board.
Labelling project:
I have attached an initial draft at a logo I tried to come up with for a business card and labelling/marketing. I am hoping that you can take this logo and 'run with it' to finesse it, make it look unique and professional.
If you need more information, please let me know.
Hello; I just wanted to let everyone know that if you feel that this brand needs a different logo, I am open to ideas (if you don't think the one I started with is ok). I am coming to the experts here!
Just to confirm also - this is related to the business card project, therefore, there are 2 projects, 2 payments! :)
Cheers
Industry/Entity Type
Business
Look and feel
Each slider illustrates characteristics of the customer's brand and the style your logo design should communicate.

```html
<!DOCTYPE html>
<html lang="en">
<head>
<meta charset="utf-8">
<title>The Brisk Owl – Dunes Bar Soap Label</title>
<link rel="stylesheet" href="https://fonts.googleapis.com/css2?family=Libre+Baskerville:wght@400;700&family=Lobster&display=swap">
<style>
  :root {
    --page: #ffffff;
    --kraft: #b99b76;
    --kraft-light: #c9ad88;
    --panel: #7b5035;
    --panel-dark: #5e3a25;
    --cream: #ecdcc0;
    --ink-dark: #3f2718;
    --berry-red: #b2382c;
    --leaf-green: #6f7d45;
  }
  html, body {
    margin: 0;
    padding: 0;
    width: 1200px;
    height: 459px;
    overflow: hidden;
    background: var(--page);
  }
  .canvas {
    position: relative;
    width: 1200px;
    height: 459px;
  }
  .label {
    position: absolute;
    left: 453px;
    top: 19px;
    width: 294px;
    height: 421px;
    background: var(--kraft);
    box-shadow: 0 1px 3px rgba(0,0,0,0.15);
  }
  .label-panel {
    position: absolute;
    inset: 13px;
    background: var(--panel);
    border: 2px solid var(--cream);
    border-radius: 14px;
  }
  .label-panel::after {
    content: "";
    position: absolute;
    inset: 5px;
    border: 1px solid var(--cream);
    border-radius: 10px;
    opacity: 0.7;
  }
  .brand-plate {
    position: absolute;
    left: 22px;
    right: 22px;
    top: 44px;
    height: 150px;
    background: var(--kraft-light);
    border: 2px solid var(--panel-dark);
    border-radius: 12px;
    display: flex;
    flex-direction: column;
    align-items: center;
    justify-content: center;
    gap: 8px;
    z-index: 1;
  }
  .brand-mark {
    width: 14px;
    height: 14px;
    border-radius: 50%;
    background: var(--ink-dark);
  }
  .brand-name,
  .brand-tagline {
    margin: 0;
    font-family: "Libre Baskerville", Georgia, serif;
    font-weight: 700;
    color: var(--ink-dark);
    text-align: center;
  }
  .brand-name { font-size: 26px; line-height: 1.1; }
  .brand-tagline { font-size: 11px; letter-spacing: 0.08em; text-transform: uppercase; }
  .product-info {
    position: absolute;
    left: 28px;
    right: 28px;
    top: 224px;
    text-align: center;
    color: var(--cream);
    z-index: 1;
  }
  .product-line {
    margin: 0;
    font-family: "Libre Baskerville", Georgia, serif;
    font-size: 12px;
  }
  .product-type {
    margin: 2px 0 0;
    font-family: "Libre Baskerville", Georgia, serif;
    font-size: 17px;
  }
  .scent-name {
    margin: 8px 0 0;
    font-family: "Lobster", cursive;
    font-size: 24px;
    color: var(--ink-dark);
  }
  .scent-rule {
    display: block;
    width: 44px;
    height: 1px;
    margin: 4px auto 10px;
    background: var(--ink-dark);
  }
  .scent-notes {
    margin: 0;
    font-family: "Libre Baskerville", Georgia, serif;
    font-size: 10.5px;
    line-height: 1.5;
  }
  .berry-sprig {
    position: absolute;
    right: 22px;
    bottom: 20px;
    width: 60px;
    height: 22px;
    border-radius: 11px;
    background: linear-gradient(90deg, var(--leaf-green), var(--berry-red));
    opacity: 0.85;
    z-index: 1;
  }
</style>
</head>
<body>
  <main class="canvas">
    <section class="label">
      <div class="label-panel"></div>

      <header class="brand-plate">
        <span class="brand-mark"></span>
        <p class="brand-name">The Brisk Owl</p>
        <p class="brand-tagline">Organic &amp; Natural Soaps</p>
      </header>

      <div class="product-info">
        <p class="product-line">Organic</p>
        <p class="product-type">Bar Soap</p>
        <p class="scent-name">Dunes</p>
        <span class="scent-rule"></span>
        <p class="scent-notes">sandalwood earthy tones with<br>a sandalwood powder exfoliant<br>to smooth your skin</p>
      </div>

      <div class="berry-sprig" role="img" aria-label="Small illustration of a leafy sprig with red berries"></div>
    </section>
  </main>
</body>
</html>
```